Ripplesound 90's Revival club night

I am after either an A5 or DL flyer but also the formats for using the design on social media etc.
The flyer is for a 90's revival club night at a nightclub that was well attended in the 90's . A special guest PA - Lulu K famous for her single 'Hold on to the starlight' ,is performing.
I have a logo for the night that may have to be altered / edited to fit in with your design (Colours changed etc) but also have a logo for the artist that may be more restrictive in regards to any changes.Both are attached.
Look forward to hearing from you shortly,

Tam

Reason: Required text to go on the flyer has now be added to the brief. Majority of designs submitted didn't seem to reflect to '90's nightclub' feel we were hoping for. Most of the designs used the colour scheme based on the 'Ripplesound' logo. We are hoping that these colours can be ignored with some designs and that the logo is made of of different colours that would make it easier for it to fit in with the designers ideas. Regards Tam

Target Market(s)

20 to 50 years age range who use to go clubbing / still do / love the 90's music. Club that they use to attend in the 90's is where the event is being held

Industry/Entity Type

Club

Requirements
Must have
• Both the logos for the event ( Ripplesound 90's Revival and Lulu K ) must be included on the flyer. Colours and the format can be altered on the ripplesound logo but the design should remain as close to the original as sent. 90's font and images would also be a must if possible. Lulu K logo can have colors altered, but not the font or design.
• Text required as follows :
• Venue : Club Vortex, Fenwick Lane, Westbury, Wiltshire
• Date : Saturday 10th June 2017
• Time : 8.30pm till 3am
• Very special guest PA ‘ LULU K’ ‘Hold on to the starlight’
• DJ’s : Main room – Dezzy Palmer ( North 38 / Ripplesound )
• Room 2 – Marcus J
• Full club décor with Laser lightshow, CO’2 cannons and pryrotechnics
• Tickets : £15 VIP / £10 General Admission – Available from : https://www.gateticketry.co.uk/venue/QWTRZN
• Or ‘Club Vortex’ : 01632 960418
• Web : www.retronightfest.co.uk
Nice to have
• open to ideas
Should not have
• Not to cheesy ........

```html
<!DOCTYPE html>
<html lang="en">
<head>
<meta charset="utf-8">
<title>Ripplesound 90's Revival – Lulu K</title>
<link rel="stylesheet" href="https://fonts.googleapis.com/css2?family=Luckiest+Guy&family=Didact+Gothic&family=Nunito+Sans:wght@400;600;700&display=swap">
<style>
  :root {
    --backdrop: #dcdde0;
    --night-deep: #140f3a;
    --night-mid: #2a2378;
    --violet: #4a1f6e;
    --glow-core: #ffffff;
    --headline-yellow: #ece230;
    --headline-shadow: #1a1440;
    --text-white: #ffffff;
    --text-ink: #1b1838;
    --band-tint: rgba(40, 24, 70, 0.55);
    --divider: rgba(255, 255, 255, 0.45);
    --display-font: "Luckiest Guy", Impact, "Arial Black", sans-serif;
    --body-font: "Didact Gothic", "Century Gothic", Arial, sans-serif;
    --info-font: "Nunito Sans", Arial, sans-serif;
  }
  * { box-sizing: border-box; margin: 0; padding: 0; }
  html, body {
    width: 1200px;
    height: 856px;
    overflow: hidden;
    background: var(--backdrop);
  }
  .poster {
    position: absolute;
    left: 290px;
    top: 0;
    width: 620px;
    height: 856px;
    overflow: hidden;
    background:
      radial-gradient(ellipse 300px 260px at 52% 48%, var(--glow-core) 0%, rgba(255,255,255,0.85) 30%, rgba(143,201,255,0.35) 60%, rgba(143,201,255,0) 100%),
      radial-gradient(ellipse 220px 200px at 50% 18%, rgba(143,201,255,0.9) 0%, rgba(80,130,230,0.4) 50%, rgba(80,130,230,0) 100%),
      radial-gradient(ellipse 200px 240px at 10% 55%, rgba(47,196,208,0.75) 0%, rgba(47,196,208,0) 100%),
      radial-gradient(ellipse 200px 220px at 92% 62%, rgba(224,88,156,0.7) 0%, rgba(224,88,156,0) 100%),
      linear-gradient(180deg, var(--night-mid) 0%, #2f3a9a 35%, var(--violet) 75%, var(--night-deep) 100%);
  }
  .poster__streaks { position: absolute; inset: 0; }
  .poster__content { position: absolute; inset: 0; text-align: center; color: var(--text-ink); }

  .event-logo {
    position: absolute;
    top: 150px; left: 0; right: 0;
    font-family: var(--display-font);
    font-size: 34px;
    color: var(--headline-yellow);
    letter-spacing: 1px;
  }
  .intro {
    position: absolute;
    top: 240px; left: 0; right: 0;
    font-family: var(--body-font);
    font-size: 23px;
    line-height: 31px;
  }
  .single-title {
    position: absolute;
    top: 308px; left: 0; right: 0;
    font-family: var(--display-font);
    font-weight: 400;
    color: var(--headline-yellow);
    text-shadow: 2px 3px 0 var(--headline-shadow);
    line-height: 1;
  }
  .single-title__line { display: block; font-size: 40px; }
  .single-title__line--big { font-size: 56px; margin-top: 6px; }
  .performing {
    position: absolute;
    top: 436px; left: 0; right: 0;
    font-family: var(--body-font);
    font-size: 26px;
    letter-spacing: 1px;
  }
  .artist-logo {
    position: absolute;
    top: 472px; left: 0; right: 0;
    font-family: var(--body-font);
    font-size: 76px;
    line-height: 1;
    color: var(--text-ink);
    letter-spacing: 4px;
  }
  .partner-badge {
    position: absolute;
    top: 560px; left: 282px;
    width: 56px; height: 18px;
    border-radius: 9px;
    background: var(--text-ink);
  }
  .date-band {
    position: absolute;
    top: 590px; left: 0; right: 0;
    height: 86px;
    background: linear-gradient(90deg, rgba(40,24,70,0) 0%, var(--band-tint) 18%, var(--band-tint) 82%, rgba(40,24,70,0) 100%);
    font-family: var(--info-font);
    color: var(--headline-yellow);
  }
  .date-band__day { display: block; margin-top: 8px; font-size: 31px; font-weight: 700; }
  .date-band__time { display: block; margin-top: 2px; font-size: 25px; font-weight: 400; }
  .info-row {
    position: absolute;
    top: 688px; left: 40px; right: 40px;
    display: flex;
    font-family: var(--info-font);
    color: var(--text-white);
  }
  .info-row__cell { flex: 1; padding: 0 6px; }
  .info-row__cell + .info-row__cell { border-left: 1px solid var(--divider); }
  .info-row__label { display: block; font-size: 18px; font-weight: 700; letter-spacing: 0.5px; }
  .info-row__value { display: block; margin-top: 4px; font-size: 14px; line-height: 18px; opacity: 0.9; }
  .info-row__price { display: block; margin-top: 0; font-size: 30px; font-weight: 700; line-height: 34px; }
  .info-row__note { display: block; font-size: 12px; line-height: 15px; opacity: 0.9; }
  .social-links {
    position: absolute;
    top: 772px; left: 0; right: 0;
    display: flex; justify-content: center; gap: 40px;
  }
  .social-links__item { width: 23px; height: 23px; background: #2b7fc8; }
  .social-links__item--second { background: #1d5f9e; }
  .social-links__item--third { background: #3559a0; }
  .fine-print {
    position: absolute;
    top: 812px; left: 20px; right: 20px;
    font-family: var(--info-font);
    font-size: 8.5px;
    line-height: 12px;
    color: var(--text-white);
    opacity: 0.85;
  }
</style>
</head>
<body>
  <main class="poster">
    <svg class="poster__streaks" width="620" height="856" viewBox="0 0 620 856" aria-hidden="true">
      <defs>
        <linearGradient id="streak-light" x1="0" y1="1" x2="1" y2="0">
          <stop offset="0" stop-color="#ffffff" stop-opacity="0"/>
          <stop offset="0.5" stop-color="#ffffff" stop-opacity="0.7"/>
          <stop offset="1" stop-color="#ffffff" stop-opacity="0"/>
        </linearGradient>
      </defs>
      <polygon points="0,740 330,470 360,470 0,775" fill="url(#streak-light)" opacity="0.55"/>
      <polygon points="0,650 300,440 315,440 0,668" fill="url(#streak-light)" opacity="0.5"/>
      <polygon points="0,590 280,420 290,420 0,602" fill="url(#streak-light)" opacity="0.4"/>
      <polygon points="0,300 260,420 260,432 0,316" fill="url(#streak-light)" opacity="0.35"/>
      <polygon points="620,540 330,470 330,480 620,560" fill="url(#streak-light)" opacity="0.35"/>
    </svg>

    <div class="poster__content">
      <div class="event-logo">Ripplesound 90's Revival</div>

      <p class="intro">A Very Special Guest PA - Lulu K<br>Famous For Her Single</p>

      <h1 class="single-title">
        <span class="single-title__line">HOLD ON TO THE</span>
        <span class="single-title__line single-title__line--big">STARLIGHT</span>
      </h1>

      <p class="performing">PERFORMING</p>
      <div class="artist-logo">LULU K</div>
      <div class="partner-badge" role="img" aria-label="Production partner badge"></div>

      <div class="date-band">
        <span class="date-band__day">Saturday 10th June 2017</span>
        <span class="date-band__time">8.30pm till 3am</span>
      </div>

      <div class="info-row">
        <div class="info-row__cell">
          <span class="info-row__label">VENUE</span>
          <span class="info-row__value">Club Vortex, Fenwick Lane<br>Westbury, Wiltshire</span>
        </div>
        <div class="info-row__cell">
          <span class="info-row__label">DJ DETAILS</span>
          <span class="info-row__value">Main: Dezzy Palmer<br>Room 2: Marcus J</span>
        </div>
        <div class="info-row__cell">
          <span class="info-row__label">TICKETS</span>
          <span class="info-row__price">£10 / £15</span>
          <span class="info-row__note">General / VIP</span>
        </div>
      </div>

      <div class="social-links" aria-label="Social links">
        <span class="social-links__item"></span>
        <span class="social-links__item social-links__item--second"></span>
        <span class="social-links__item social-links__item--third"></span>
      </div>

      <p class="fine-print">Full club décor with laser lightshow, CO2 cannons and pyrotechnics · Tickets: https://www.gateticketry.co.uk/venue/QWTRZN<br>or Club Vortex: 01632 960418 · www.retronightfest.co.uk</p>
    </div>
  </main>
</body>
</html>
```